Business Card Design (NEW FILES)

ATTENTION: New vector files are available. Please update your design to reflect/use the new (better resolution) logo images.

Seeking a unique and professional business card design for a commercial drone photography/videography business. The layout should feature
the logo (attached) and include the following information:
Pete Varner
978-552-6170
www.skylarkvisuals.example
NVR Certified Remote Pilot

Pete Varner

```html
<!DOCTYPE html>
<html lang="en">
<head>
<meta charset="utf-8">
<title>Skylark Visuals – Business Card</title>
<link rel="stylesheet" href="https://fonts.googleapis.com/css2?family=Arimo:ital,wght@0,400;0,700;1,700&display=swap">
<style>
  :root {
    --navy: #131a4d;
    --orange: #eb874b;
    --white: #ffffff;
    --stage: #1b1b1d;
    --ink-soft: #2a3170;
  }
  * { margin: 0; padding: 0; box-sizing: border-box; }
  html, body {
    width: 1200px; height: 963px; overflow: hidden;
    background: var(--stage);
    font-family: "Arimo", Arial, sans-serif;
  }
  .card {
    position: absolute; left: 100px; top: 196px;
    width: 1000px; height: 571px;
    background: var(--white);
    border-radius: 34px;
    overflow: hidden;
  }
  .brand {
    position: absolute; left: 64px; top: 58px;
    display: flex; align-items: center; gap: 16px;
  }
  .brand-dot {
    width: 34px; height: 34px; border-radius: 50%;
    background: var(--navy);
  }
  .brand-name {
    font-size: 46px; font-weight: 400; letter-spacing: 3px;
    color: var(--navy); text-transform: uppercase; line-height: 1;
  }
  .contact {
    position: absolute; left: 64px; top: 232px;
    list-style: none; color: var(--navy);
    font-size: 25px; line-height: 1;
  }
  .contact li { display: flex; align-items: center; gap: 14px; margin-bottom: 18px; }
  .contact svg { width: 22px; height: 22px; flex: none; }
  .drone-art {
    position: absolute; left: 520px; top: 330px; width: 480px; height: 241px;
    background: linear-gradient(160deg, var(--ink-soft) 0%, var(--navy) 70%);
    border-radius: 140px 0 0 0;
  }
  .person {
    position: absolute; right: 70px; top: 200px; text-align: right;
  }
  .person-name {
    font-size: 34px; font-weight: 700; letter-spacing: 1px;
    color: var(--navy); text-transform: uppercase; line-height: 1;
  }
  .person-name .surname { color: var(--orange); }
  .person-role { font-size: 24px; color: var(--navy); margin-top: 8px; }
  .name-tab {
    position: absolute; right: 0; top: 212px;
    width: 44px; height: 66px; background: var(--orange);
  }
  .band-cert {
    position: absolute; left: 0; top: 386px; width: 100%; height: 82px;
    background: var(--navy);
    display: flex; align-items: center; padding-left: 64px;
    color: var(--white); font-size: 27px;
  }
  .band-insured {
    position: absolute; left: 0; top: 468px; width: 100%; height: 103px;
    background: var(--orange);
    display: flex; align-items: flex-start; padding: 22px 0 0 64px;
    color: var(--white); font-size: 28px; font-weight: 700; font-style: italic;
  }
</style>
</head>
<body>
  <main class="card">
    <div class="brand">
      <span class="brand-dot"></span>
      <span class="brand-name">Skylark Visuals</span>
    </div>

    <ul class="contact">
      <li>
        <svg viewBox="0 0 24 24" aria-hidden="true"><path fill="#eb874b" d="M6.6 10.8a15.1 15.1 0 0 0 6.6 6.6l2.2-2.2a1 1 0 0 1 1-.25 11.4 11.4 0 0 0 3.6.57 1 1 0 0 1 1 1V20a1 1 0 0 1-1 1A17 17 0 0 1 3 4a1 1 0 0 1 1-1h3.5a1 1 0 0 1 1 1c0 1.25.2 2.45.57 3.57a1 1 0 0 1-.25 1z"/></svg>
        978-552-6170
      </li>
      <li>
        <svg viewBox="0 0 24 24" aria-hidden="true"><g fill="none" stroke="#eb874b" stroke-width="2"><circle cx="12" cy="12" r="9"/><path d="M3 12h18M12 3c3 3.2 3 14.8 0 18M12 3c-3 3.2-3 14.8 0 18"/></g></svg>
        www.skylarkvisuals.example
      </li>
    </ul>

    <div class="band-cert">NVR Certified Remote Pilot</div>
    <div class="band-insured">Fully Insured</div>

    <div class="drone-art" role="img" aria-label="Large navy silhouette of a camera drone with a spinning rotor, filling the lower right of the card"></div>

    <div class="name-tab"></div>
    <div class="person">
      <p class="person-name">Pete <span class="surname">Varner</span></p>
      <p class="person-role">Owner</p>
    </div>
  </main>
</body>
</html>
```